Geschäftspapiere für Beratungsleistung
Zielgruppe
DieKlarwerkstatt.com ist eine Beratungsleistung der Voltrin Consulting GmbH.
Wir beraten kleine und mittlere Unternehmen (B2B) in Fragen des Datenschutz. Wir unterstützen unsere Kunden dabei, die notwendigen Richtlinien, Dokumentationen und Prozesse einzuführen, die sicherstellen, dass unsere Kunden die gesetzlichen Vorgaben zum Schutz personenbezogener Daten einhalten.
Aufgabenstellung
Wichtiger Hinweis: Wir möchten die Gestaltung von Briefpapier und Visitenkarten beauftragen. Da grafikfinder.de das nicht als Standardprojekt mit entsprechender Preisskala vorsieht, haben wir einen individuellen Preis festgelegt (160 Euro Briefbogen + 120 Euro Visitenkarten).
'Die Klarwerkstatt' ist eine Marke der Voltrin Consulting GmbH. Das Markenlogo ist bereits vorhanden.
Die Aufgabenstellung ist es, einen Briefbogen mit den Geschäftsangaben, sowie einen Folgebogen ohne Geschäftsangaben zu entwickeln. Außerdem sollen Visitenkarten entworfen werden.
Die Geschäftspapiere sollen sich in der Gestaltung an die Website von 'Die Klarwerkstatt' anlehnen. Da die Website noch nicht live sind, ist der Entwurf der Homepage angehängt. Wichtig: die im Banner verwendete Teaser-Grafik soll nicht als Hintergrund für die Geschäftspapiere verwendet werden.
Bitte beachten Sie, dass 'Die Klarwerkstatt' kein Unternehmen ist, sondern eine Marke der Voltrin Consulting ist. Die Angaben auf den Geschäftspapieren beziehen sich daher auf die Voltrin Consulting GmbH. Der Briefbogen der Voltrin Consulting ist angehängt. Dort können die Geschäftsangaben entnommen werden. Das Voltrin Logo soll auf den Geschäftspapieren für 'Die Klarwerkstatt' nicht verwendet werden. Der Entwurf soll auf das Logo und Erscheinungsbild von 'Die Klarwerkstatt' abgestellt werden.
Die Entwürfe möchten wir zum einen im Indesign-Format haben, um diese an einen Druckdienstleister weiterzugeben bzw. die entsprechenden pdfs nach Vorgaben der Druckerei erzeugen zu können. Den Briefbogen und den Folgebogen möchten wir außerdem im Microsoft Word-Format haben, um Geschäftsbriefe direkt aus Word heraus zu erzeugen zu können. Die Dokumente sollen dann entweder als pdf per E-Mail versendet oder auf einem Tintenstrahldrucker gedruckt werden. Das Design sollte also auch auf einem Büro-Farbtintenstrahldrucker in guter Darstellung gedruc..

```html
<!DOCTYPE html>
<html lang="de">
<head>
<meta charset="utf-8">
<title>Die Klarwerkstatt – Geschäftspapiere</title>
<link rel="stylesheet" href="https://fonts.googleapis.com/css2?family=Source+Sans+3:wght@400&family=Ubuntu:wght@400;500&display=swap">
<style>
  :root{
    --stage:#3d4b5f;
    --brand-blue:#0b4f98;
    --brand-orange:#f39200;
    --ink:#1d1d1b;
    --ink-soft:#4a4a4a;
    --paper:#ffffff;
    --rule:#5a5a5a;
  }
  *{margin:0;padding:0;box-sizing:border-box}
  html,body{width:1200px;height:1026px;overflow:hidden}
  body{background:var(--stage);position:relative;font-family:"Ubuntu",sans-serif;color:var(--ink-soft)}

  .card{position:absolute;width:270px;height:174px;box-shadow:0 4px 14px rgba(0,0,0,.35)}
  .card--front{background:var(--paper)}
  .card--back{background:var(--brand-blue);color:#fff}

  .brand{display:flex;align-items:center;gap:6px;font-family:"Ubuntu",sans-serif;font-weight:500;color:var(--brand-blue);line-height:.95;letter-spacing:.2px}
  .brand__mark{background:var(--brand-orange);flex:none}
  .brand--light{color:#fff}

  .card .brand{position:absolute;left:0;right:0;justify-content:center}
  .card--front .brand{top:20px;font-size:12.5px}
  .card--front .brand__mark{width:18px;height:18px}
  .card--back .brand{top:68px;font-size:16px}
  .card--back .brand__mark{width:22px;height:22px}

  .card__name{position:absolute;top:78px;width:100%;text-align:center;font-size:8.2px;color:var(--ink-soft)}
  .card__name strong{color:var(--brand-blue);font-weight:500}
  .card__company{position:absolute;top:110px;width:100%;text-align:center;font-size:7px;line-height:10px}
  .card__company b{font-weight:500}
  .card__rule{position:absolute;top:136px;left:15px;right:17px;height:1.4px;background:var(--brand-blue)}
  .card__contacts{position:absolute;top:142px;left:16px;right:16px;display:flex;justify-content:space-between;font-size:7px;line-height:11px}
  .contact-row{display:flex;align-items:center;gap:5px}
  .contact-row svg{width:7px;height:7px;fill:var(--brand-blue);flex:none}
  .card__url{position:absolute;top:139px;width:100%;text-align:center;font-size:7.3px}

  .letter{position:absolute;left:489px;top:49px;width:664px;height:939px;background:var(--paper);box-shadow:0 4px 18px rgba(0,0,0,.35)}
  .letter .brand{position:absolute;left:464px;top:50px;font-size:14px}
  .letter .brand__mark{width:20px;height:20px}
  .letter__contacts{position:absolute;left:464px;top:115px;font-size:7.6px;line-height:10.2px}
  .letter__contacts svg{width:7px;height:7px;fill:var(--brand-blue)}
  .letter__sender{position:absolute;left:67px;top:145px;font-size:7.4px;color:var(--brand-blue)}
  .fold-mark{position:absolute;left:0;width:24px;height:1px;background:#b5b5b5}

  .letter__text{position:absolute;left:67px;width:540px;font-family:"Source Sans 3",sans-serif;font-size:13.4px;line-height:16.2px;color:var(--ink);hyphens:auto}
  .letter__recipient{top:172px}
  .letter__subject{top:288px}
  .letter__body{top:329px}
  .letter__body p{margin-bottom:16.2px}

  .letter__footer{position:absolute;left:48px;top:840px;right:37px}
  .footer-mark{position:absolute;left:0;top:0;width:13px;height:13px;background:var(--brand-blue)}
  .footer-rule{position:absolute;left:38px;right:0;top:6px;height:2px;background:var(--rule)}
  .footer-brand{position:absolute;left:18px;top:22px;font-size:7.4px;font-weight:500;color:var(--brand-blue)}
  .footer-col{position:absolute;top:33px;font-size:7px;line-height:9.6px;color:var(--ink-soft)}
  .footer-col b{font-weight:500}
</style>
</head>
<body>

<svg width="0" height="0" style="position:absolute">
  <defs>
    <symbol id="ic-phone" viewBox="0 0 10 10"><path d="M2 0.5 3.6 2.6 2.6 3.6C3.2 5 5 6.8 6.4 7.4L7.4 6.4 9.5 8 8.4 9.5C4.5 9.5 0.5 5.5 0.5 1.6Z"/></symbol>
    <symbol id="ic-fax" viewBox="0 0 10 10"><path d="M2.5 0.5H7.5V3H2.5ZM0.5 3.5H9.5V8H7.5V9.5H2.5V8H0.5ZM3.3 6.2V8.7H6.7V6.2Z"/></symbol>
    <symbol id="ic-mail" viewBox="0 0 10 10"><path d="M0.5 2H9.5V8H0.5ZM1.3 2.6 5 5.5 8.7 2.6Z"/></symbol>
    <symbol id="ic-web" viewBox="0 0 10 10"><path d="M5 0.5A4.5 4.5 0 1 0 5 9.5 4.5 4.5 0 1 0 5 0.5ZM5 1.4C5.6 2 6 3.3 6.1 4.6H3.9C4 3.3 4.4 2 5 1.4ZM1.4 5.4H3.1C3.2 6.5 3.4 7.5 3.8 8.3 2.5 7.8 1.6 6.7 1.4 5.4ZM6.9 5.4H8.6C8.4 6.7 7.5 7.8 6.2 8.3 6.6 7.5 6.8 6.5 6.9 5.4ZM3.9 5.4H6.1C6 6.7 5.6 8 5 8.6 4.4 8 4 6.7 3.9 5.4Z"/></symbol>
  </defs>
</svg>

<!-- Visitenkarte Helene Dorwald, Vorderseite -->
<section class="card card--front" style="left:58px;top:69px">
  <div class="brand"><span class="brand__mark"></span><span>DIE<br>KLARWERKSTATT</span></div>
  <p class="card__name"><strong>Helene Dorwald</strong> - Geschäftsführerin</p>
  <p class="card__company"><b>Voltrin Consulting GmbH</b><br>Lindenhofweg 7 B - 82049 Pullach</p>
  <div class="card__rule"></div>
  <div class="card__contacts">
    <div>
      <div class="contact-row"><svg><use href="#ic-phone"/></svg>+49 89 507318-00</div>
      <div class="contact-row"><svg><use href="#ic-fax"/></svg>+49 89 507318-09</div>
    </div>
    <div>
      <div class="contact-row"><svg><use href="#ic-mail"/></svg>dorwald@voltrin-consulting.de</div>
      <div class="contact-row"><svg><use href="#ic-web"/></svg>www.voltrin-consulting.de</div>
    </div>
  </div>
</section>

<!-- Visitenkarte Rückseite -->
<section class="card card--back" style="left:58px;top:261px">
  <div class="brand brand--light"><span class="brand__mark"></span><span>DIE<br>KLARWERKSTATT</span></div>
  <p class="card__url">www.die-klarwerkstatt.com</p>
</section>

<!-- Visitenkarte Jonas Kellert, Vorderseite -->
<section class="card card--front" style="left:162px;top:479px;width:273px;height:176px">
  <div class="brand"><span class="brand__mark"></span><span>DIE<br>KLARWERKSTATT</span></div>
  <p class="card__name"><strong>Jonas Kellert</strong> - Geschäftsführer</p>
  <p class="card__company"><b>Voltrin Consulting GmbH</b><br>Lindenhofweg 7 B - 82049 Pullach</p>
  <div class="card__rule"></div>
  <div class="card__contacts">
    <div>
      <div class="contact-row"><svg><use href="#ic-phone"/></svg>+49 89 507318-00</div>
      <div class="contact-row"><svg><use href="#ic-fax"/></svg>+49 89 507318-09</div>
    </div>
    <div>
      <div class="contact-row"><svg><use href="#ic-mail"/></svg>kellert@voltrin-consulting.de</div>
      <div class="contact-row"><svg><use href="#ic-web"/></svg>www.voltrin-consulting.de</div>
    </div>
  </div>
</section>

<!-- Visitenkarte Rückseite -->
<section class="card card--back" style="left:161px;top:673px;width:273px;height:176px">
  <div class="brand brand--light"><span class="brand__mark"></span><span>DIE<br>KLARWERKSTATT</span></div>
  <p class="card__url" style="top:141px">www.die-klarwerkstatt.com</p>
</section>

<!-- Briefbogen -->
<article class="letter">
  <div class="brand"><span class="brand__mark"></span><span>DIE<br>KLARWERKSTATT</span></div>

  <div class="letter__contacts">
    <div class="contact-row"><svg><use href="#ic-phone"/></svg>+49 89 507318-00</div>
    <div class="contact-row"><svg><use href="#ic-fax"/></svg>+49 89 507318-09</div>
    <div class="contact-row"><svg><use href="#ic-mail"/></svg>info@die-klarwerkstatt.com</div>
    <div class="contact-row"><svg><use href="#ic-web"/></svg>www.die-klarwerkstatt.com</div>
  </div>

  <p class="letter__sender">Voltrin Consulting GmbH - Lindenhofweg 7 B - 82049 Pullach</p>

  <span class="fold-mark" style="top:274px"></span>
  <span class="fold-mark" style="top:468px;width:34px"></span>
  <span class="fold-mark" style="top:607px"></span>

  <address class="letter__text letter__recipient" style="font-style:normal">
    Firma Berger und Partner<br>Herr Berger<br>Amselweg 45<br>44135 Dortmund<br>Deutschland
  </address>

  <p class="letter__text letter__subject">Betreffzeile</p>

  <div class="letter__text letter__body">
    <p>Sehr geehrte Damen und Herren,</p>
    <p>schön, dass Sie neugierig reinschauen, obwohl hier ja eigentlich noch gar kein richtiger Text steht, sondern nur der sogenannte Blindtext. Dieser Blindtext will Ihnen nämlich sagen: Erstens will er den Texter entschuldigen – tut uns leid, aber es war einfach unmöglich, das Ding gestern Nacht noch exakt auf Länge runterzuschreiben. Das Briefing, Sie wissen schon. Schwieriges Thema. Und die Freundin ist krank, und der Freund wollte in diesen neuen Film. Und dann hat sich der Film so überhaupt nicht gelohnt, sagte er.</p>
    <p>Ja, und zweitens haben wir Sie bis hierhin zum Lesen gebracht und wollen damit belegen, dass nicht alle Marktforscher und Kaffeesatzleser recht haben, die sagen, dass unser armer Freund Otto Normalverbraucher und seine hässliche Schwester Lieschen Müller maximal Null Komma gar kein Interesse haben für Texte.</p>
    <p>Drittens sollten wir für ein paar Zeilen abschweifen und uns dem Gegenstand unserer Bemühungen zuwenden. Was heißt überhaupt Blindtext? Macht er blind, und wenn ja, wen? Ich denke, das Wörtchen will uns ja auch nur warnend darauf hinweisen, dass viel zu oft nach dem Motto „Augen zu und durch“ verfahren wird bei der verantwortungsvollen Aufgabe, Grauwert zu verteilen.</p>
    <p>Erstens will er den Texter entschuldigen – tut uns leid, aber es war einfach unmöglich, das Ding gestern Nacht noch exakt auf Länge runterzuschreiben. Das Briefing, Sie wissen schon. Schwieriges Thema. Und die Freundin ist krank, und der Freund wollte in diesen neuen Film. Und dann hat sich der Film so überhaupt nicht gelohnt, sagte er.</p>
    <p>Mit freundlichen Grüßen,</p>
    <p>Lena Beispiel</p>
  </div>

  <footer class="letter__footer">
    <span class="footer-mark"></span>
    <div class="footer-rule"></div>
    <p class="footer-brand">DIE KLARWERKSTATT</p>
    <p class="footer-col" style="left:18px"><b>Voltrin Consulting GmbH<br>Lindenhofweg 7 B<br>D-82049 Pullach</b></p>
    <p class="footer-col" style="left:195px"><b>Geschäftsführer:</b><br>Helene Dorwald<br>Jonas Kellert</p>
    <p class="footer-col" style="left:331px"><b>Amtsgericht München</b><br>HRB 318207<br>USt-ID: DE301457826</p>
    <p class="footer-col" style="left:473px">Die Klarwerkstatt<br>ist ein Beratungsangebot<br>der Voltrin Consulting GmbH</p>
  </footer>
</article>

</body>
</html>
```